Business software developers new website

We need to redesign our website. Our current website is http://www.plumvista.net/index.html, which is outdated and needs a new look. We moved out from web design and have concentrated more on the back end of the systems, for example, system support and security and cloud-based applications. Our major clients include both private and government sectors. We would like to see some designs that are all in one page, simple and clean. Prefer illustrator or obstructed images instead of real-life photos. Must look futuristic yet friendly. Attached the new logo for your references and good luck.

Target Market(s)

Medium to big company for their IT or data management. Either improve or upgrade their current system.

Industry/Entity Type

Business Software

Number of Pages Required

1 page

Colors

Designer to choose colors to be used in the design.

Requirements
Must have
• Simple and clean. Individual assets must be provided in the correct size and format(png or jpeg). Prefer Goggle fonts. Even though the logo color is red, grey and black, still prefer some modern colors that go well with red. When design, must consider the possibility to convert it into responsive.
Nice to have
• White background
Should not have
• real life photos, no slider

```html
<!DOCTYPE html>
<html lang="en">
<head>
<meta charset="utf-8">
<title>Plumvista — Cloud Based Applications</title>
<link href="https://fonts.googleapis.com/css2?family=Poppins:wght@400;500;600;700&family=Lora:ital,wght@1,500&display=swap" rel="stylesheet">
<style>
:root{
  --blue:#0b5bd3;
  --blue-dark:#0a3d8f;
  --navy:#12233f;
  --ink:#111722;
  --muted:#6b7383;
  --line:#c9d3e6;
  --star:#e6d21a;
  --white:#ffffff;
  --red:#d8262c;
}
*{margin:0;padding:0;box-sizing:border-box}
html,body{width:1200px;height:2852px;overflow:hidden;background:var(--white)}
body{position:relative;font-family:"Poppins",Arial,sans-serif;color:var(--ink)}
.abs{position:absolute}

/* header */
.brand{left:120px;top:44px;display:flex;align-items:center;gap:10px}
.brand-dot{width:20px;height:20px;border-radius:50%;background:var(--red)}
.brand-name{font-size:24px;font-weight:600;color:var(--navy);letter-spacing:-0.5px;white-space:nowrap}
.nav{left:362px;top:58px;display:flex;gap:46px;font-size:15px;font-weight:500;color:var(--navy)}
.nav a{color:inherit;text-decoration:none}
.nav .active{color:var(--blue);border-bottom:2px solid var(--blue);padding-bottom:4px}
.phone-pill{left:792px;top:52px;width:170px;height:36px;border-radius:18px;background:var(--navy);color:var(--white);font-size:14px;font-weight:600;display:flex;align-items:center;justify-content:center}
.menu-toggle{left:1068px;top:58px;width:28px}
.menu-toggle span{display:block;height:3px;background:var(--navy);margin-bottom:6px;border-radius:2px}

/* hero */
.hero-title{left:140px;top:176px;font-size:66px;font-weight:700;line-height:1.2;color:var(--ink);white-space:nowrap}
.btn-contact{left:140px;top:472px;width:292px;height:76px;border-radius:38px;background:var(--blue);color:var(--white);font-size:30px;font-weight:600;display:flex;align-items:center;justify-content:center}
.hero-art{left:670px;top:100px;width:400px;height:510px;border-radius:30px;background:radial-gradient(circle at 50% 55%,#cfe0fb 0%,#e9f1fd 55%,#ffffff 80%)}

.divider{left:140px;width:920px;height:2px;background:var(--line)}

/* services */
.section-title{left:0;width:1200px;top:786px;text-align:center;font-size:44px;font-weight:600}
.section-lead{left:350px;width:500px;top:866px;text-align:center;font-size:16px;font-weight:600;line-height:1.6}
.service{width:260px;text-align:center}
.service-icon{width:62px;height:62px;margin:0 auto 18px;border-radius:50%;border:2px solid var(--blue);display:flex;align-items:center;justify-content:center}
.service-title{font-size:15px;font-weight:600;margin-bottom:16px}
.service-text{font-size:13px;color:var(--muted);line-height:1.7}
.btn-more{left:516px;top:1528px;width:168px;height:36px;border-radius:18px;background:var(--blue);color:var(--white);font-size:12px;font-weight:600;letter-spacing:1px;display:flex;align-items:center;justify-content:center}

/* testimonial */
.portrait{left:420px;top:1675px;width:360px;height:360px;border-radius:50%;background:linear-gradient(160deg,#cfe8e4,#6fb7a8 60%,#3d6b66)}
.avatar{border-radius:50%;background:linear-gradient(150deg,#8c6a55,#3b2c26);box-shadow:0 0 26px 10px rgba(230,120,190,.35)}
.avatar.cool{box-shadow:0 0 26px 10px rgba(80,150,255,.35)}
.stars{left:0;width:1200px;top:2068px;text-align:center;font-size:58px;letter-spacing:4px;color:var(--star);line-height:1}
.quote{left:320px;width:560px;top:2128px;text-align:center;font-family:"Lora",Georgia,serif;font-style:italic;font-size:31px;line-height:1.6;color:var(--navy)}
.quote-mark{font-family:"Lora",Georgia,serif;font-size:110px;color:var(--blue);line-height:1;font-weight:500}
.author{left:0;width:1200px;top:2282px;text-align:center;font-size:13px;color:var(--muted)}
.author b{color:var(--blue);font-weight:600}
.arrow-left{left:118px;top:2178px;width:30px;height:30px;border-radius:50%;background:var(--blue)}
.arrow-right{left:1046px;top:2178px;width:30px;height:30px;border-radius:50%;border:1.5px solid var(--line)}

/* footer */
.footer-wave{left:0;top:2380px;width:1200px;height:472px}
.footer-brand{left:116px;top:2562px;background:var(--white);padding:6px 10px;display:flex;align-items:center;gap:6px}
.footer-brand .brand-dot{width:14px;height:14px}
.footer-brand .brand-name{font-size:19px}
.f-col{top:2540px;color:var(--white);font-size:12px;line-height:2}
.f-col h4{font-size:12px;font-weight:600;letter-spacing:2px;margin-bottom:8px}
.f-col h4::after{content:"";display:block;width:20px;height:2px;background:var(--white);margin-top:2px}
.f-social{display:flex;gap:26px;margin-top:8px}
.f-social span{width:18px;height:18px;border-radius:50%;background:var(--white)}
.copyright{left:0;width:1200px;top:2798px;text-align:center;color:#b9cdf3;font-size:11px}
</style>
</head>
<body>

<header>
  <div class="abs brand"><span class="brand-dot"></span><span class="brand-name">plumvista.net</span></div>
  <nav class="abs nav">
    <a class="active">Home</a><a>Services</a><a>Work</a><a>About</a>
  </nav>
  <div class="abs phone-pill">(01) 555 - 010 - 220</div>
  <div class="abs menu-toggle"><span></span><span></span><span></span></div>
</header>

<section class="hero">
  <div class="abs hero-art" role="img" aria-label="Isometric illustration of blue server racks connected to a cloud"></div>
  <h1 class="abs hero-title">Cloud<br>Based<br>Applications</h1>
  <div class="abs btn-contact">contact us</div>
</section>

<div class="abs divider" style="top:728px"></div>

<section class="services">
  <h2 class="abs section-title">Our services</h2>
  <p class="abs section-lead">Quam adipiscing vitae proin sagittis nisl rhoncus mattis rhoncus urna. Quam elementum pulvinar etiam non. Eu consequat.</p>

  <div class="abs service" style="left:154px;top:996px">
    <div class="service-icon"><svg width="28" height="28" viewBox="0 0 28 28" fill="none" stroke="#0b5bd3" stroke-width="2"><circle cx="14" cy="14" r="10"/><path d="M4 14h20M14 4c4 4 4 16 0 20M14 4c-4 4-4 16 0 20"/></svg></div>
    <div class="service-title">Webdesign</div>
    <p class="service-text">Tincidunt lobortis feugiat vivamus at augue eget. Risus feugiat in ante metus dictum amet.</p>
  </div>
  <div class="abs service" style="left:474px;top:996px">
    <div class="service-icon"><svg width="28" height="28" viewBox="0 0 28 28" fill="none" stroke="#0b5bd3" stroke-width="2"><circle cx="14" cy="9" r="4"/><path d="M6 23c0-5 4-8 8-8s8 3 8 8"/></svg></div>
    <div class="service-title">Webdev</div>
    <p class="service-text">Eget nulla facilisi etiam dignissim diam quis enim lobortis scelerisque. Eu feugiat pretium nibh.</p>
  </div>
  <div class="abs service" style="left:806px;top:996px">
    <div class="service-icon"><svg width="28" height="28" viewBox="0 0 28 28" fill="none" stroke="#0b5bd3" stroke-width="2"><rect x="8" y="3" width="12" height="22" rx="2"/><path d="M12 21h4"/></svg></div>
    <div class="service-title">Marketing</div>
    <p class="service-text">Eu augue ut lectus arcu bibendum at. Pellentesque nec nam aliquam sem et tortor.</p>
  </div>

  <div class="abs service" style="left:154px;top:1256px">
    <div class="service-icon"><svg width="28" height="28" viewBox="0 0 28 28" fill="none" stroke="#0b5bd3" stroke-width="2"><path d="M6 22l4-1 12-12-3-3L7 18z"/></svg></div>
    <div class="service-title">Marketing</div>
    <p class="service-text">Ut venenatis a condimentum vitae sapien. Magna fermentum iaculis eu non diam phasellus.</p>
  </div>
  <div class="abs service" style="left:474px;top:1256px">
    <div class="service-icon"><svg width="28" height="28" viewBox="0 0 28 28" fill="none" stroke="#0b5bd3" stroke-width="2"><circle cx="10" cy="10" r="3"/><circle cx="18" cy="10" r="3"/><path d="M4 22c0-4 3-7 6-7s6 3 6 7M14 22c0-4 2-7 4-7s6 3 6 7"/></svg></div>
    <div class="service-title">Webdesign</div>
    <p class="service-text">Sollicitudin ac orci phasellus egestas tellus rutrum tellus pellentesque. Malesuada fames ac turpis.</p>
  </div>
  <div class="abs service" style="left:806px;top:1256px">
    <div class="service-icon"><svg width="28" height="28" viewBox="0 0 28 28" fill="none" stroke="#0b5bd3" stroke-width="2"><circle cx="14" cy="14" r="10"/><path d="M14 8v6l4 3"/></svg></div>
    <div class="service-title">Webdev</div>
    <p class="service-text">Integer quis auctor elit sed vulputate mi. Semper auctor neque vitae tempus quam.</p>
  </div>

  <div class="abs btn-more">LEARN MORE</div>
</section>

<div class="abs divider" style="top:1624px"></div>

<section class="testimonial">
  <div class="abs avatar" role="img" aria-label="Client portrait" style="left:54px;top:1762px;width:48px;height:48px"></div>
  <div class="abs avatar cool" role="img" aria-label="Client portrait" style="left:190px;top:1830px;width:36px;height:36px"></div>
  <div class="abs avatar" role="img" aria-label="Client portrait" style="left:86px;top:2030px;width:60px;height:60px"></div>
  <div class="abs avatar cool" role="img" aria-label="Client portrait" style="left:340px;top:1966px;width:52px;height:52px"></div>
  <div class="abs avatar cool" role="img" aria-label="Client portrait" style="left:834px;top:1962px;width:60px;height:60px"></div>
  <div class="abs avatar" role="img" aria-label="Client portrait" style="left:946px;top:1894px;width:40px;height:40px"></div>
  <div class="abs avatar cool" role="img" aria-label="Client portrait" style="left:1064px;top:1806px;width:66px;height:66px"></div>
  <div class="abs avatar" role="img" aria-label="Client portrait" style="left:1086px;top:1980px;width:50px;height:50px"></div>

  <div class="abs portrait" role="img" aria-label="Portrait of a smiling client on the phone"></div>

  <div class="abs stars">★★★★★</div>
  <span class="abs quote-mark" style="left:236px;top:2090px">“</span>
  <p class="abs quote">Plumvista offers amazing services and quality applications</p>
  <span class="abs quote-mark" style="left:820px;top:2180px">”</span>
  <p class="abs author"><b>Dana Ruelle</b> – Some Company</p>

  <div class="abs arrow-left"></div>
  <div class="abs arrow-right"><svg width="27" height="27" viewBox="0 0 27 27" fill="none" stroke="#6b7383" stroke-width="1.5"><path d="M12 9l4 4.5-4 4.5"/></svg></div>
</section>

<footer>
  <svg class="abs footer-wave" viewBox="0 0 1200 472" preserveAspectRatio="none">
    <path d="M0 70 C200 10 380 20 600 60 C820 100 1000 90 1200 40 L1200 472 L0 472 Z" fill="#0b5bd3"/>
  </svg>
  <div class="abs footer-brand"><span class="brand-dot"></span><span class="brand-name">plumvista.net</span></div>

  <div class="abs f-col" style="left:360px">
    <h4>MENU</h4>
    Home<br>About<br>Services<br>Work<br>Gallery<br>Contact
  </div>
  <div class="abs f-col" style="left:445px">
    <h4>SERVICES</h4>
    Loren<br>Ipsum<br>Dolor<br>Sit Amet
  </div>
  <div class="abs f-col" style="left:606px">
    <h4>CONTACT US</h4>
    ✉ &nbsp;hello@plumvista.net<br>☎ &nbsp;(01) 555 - 010 - 220
  </div>
  <div class="abs f-col" style="left:850px">
    <h4>FOLLOW US</h4>
    <div class="f-social"><span></span><span></span><span></span><span></span></div>
  </div>

  <p class="abs copyright">© 2024 Plumvista. All rights reserved.</p>
</footer>

</body>
</html>
```